Progressive business consultancy seeking innovative and clever powerpoint design

Were looking for a PowerPoint design for our Melbourne based business consulting company, Vantora.

About Us:
Based in Melbourne, Australia, Vantora is a management consulting organisation that partners with their clients to lead the execution of strategic process and system improvement initiatives.

Vantora offers business advisory services in Project Management, Business Process Management, Change Management, Business Analysis and Business Intelligence. Vantora combines hands on delivery with coaching in best practice methodologies and approaches to build our clients capabilities ensuring their ongoing success in project implementations.

Vantora has extensive experience across a wide range of industries. We specialise in assisting organisations across the accounting, legal, financial services and health sectors.

Our core purpose is to help businesses in the middle market navigate transformational change through clear and focused execution and enablement.

www.vantora.com.au
@vantora_hq

What we're looking for:
A PowerPoint template consisting of:
- a front/cover page with hero image (attached)
- a contents page
- a divider page (for different segments of the slide deck)
- a standard PowerPoint content page
- a blank PowerPoint page. (still Vantora themed)

The Vantora colours are white and blue (RGB:0/86/162 and
CMYK 97/73/4/0)

All slides should have the Vantora logo (attached) and a professional, almost corporate, (but not boring) theme that is consistent across all slides. The design should reflect our focus on the "e" in vantora, which is what we're really about - "e"xecution and "e"nablement of change.

I've attached a PNG file of our word template which shows the focus on the "e" as a watermark on the document as well as the font files if required.

Let me know if you need any further information or design specifics.

Thanks,

Marjorie
(on behalf of Desmond)
Updates

Project Deadline Extended
Reason: Hi Designers, We have received some really great designs. Thanks for taking the time to make your submissions. We have decided to extend the deadline as we need some more time to review and consult other colleagues on the great submissions we have received. We are also hoping we might get some additional submissions over the weekend. We would also like enough time to provide feedback on all the submissions received. Thanks for helping us out with some really creative work. Desmond @vantora_hq

Project Deadline Extended
Reason: Hi designers, thanks for taking the time to submit your designs. We have some really great submissions. We are going to have to extend our deadline again as we just haven't had the chance to review and provide feedback on all the designs. We will be closing this project off on Tuesday March 17. Thanks Desmond @vantora_hq

Target Market(s)

C-Level executives (CEO,COO,CIO) at professional services firms (Accounting and Legal), not for profit organisations and financial services firms.

Industry/Entity Type

Management Consulting

Font styles to use
Serif
Other font styles liked:
• Calibri or attached fonts

Requirements
Must have
• A PowerPoint template consisting of:
• 1) a front/cover page with hero image (attached)
• 2) a contents page
• 3) a divider page (for different segments of the slide deck)
• 4) a standard PowerPoint content page
• 5) a blank PowerPoint page. (still Vantora themed)
• 6) Two content
• 7) Comparison
• 8) Table
• 9) Picture column
• 10) Chevron
• The Vantora colours are white and blue (RGB:0/86/162 and
• CMYK 97/73/4/0)

```html
<!DOCTYPE html>
<html lang="en">
<head>
<meta charset="utf-8">
<title>Vantora – Content Slide</title>
<link rel="stylesheet" href="https://fonts.googleapis.com/css2?family=Questrial&display=swap">
<style>
  :root {
    --brand-blue: #0056a2;
    --header-deep: #163f8c;
    --header-light: #2a5fb4;
    --title-blue: #1d5fae;
    --body-grey: #9a9a9a;
    --white: #ffffff;
  }
  * { margin: 0; padding: 0; box-sizing: border-box; }
  html, body { width: 1200px; height: 900px; overflow: hidden; background: var(--white); }
  body { font-family: "Questrial", "Century Gothic", sans-serif; }

  .slide { position: relative; width: 1200px; height: 900px; background: var(--white); overflow: hidden; }

  .slide-header {
    position: absolute; left: 0; top: 0; width: 1200px; height: 95px;
    background: linear-gradient(90deg, var(--header-deep) 0%, var(--header-light) 55%, var(--header-deep) 100%);
  }
  .slide-title {
    position: absolute; left: 27px; top: 22px;
    color: var(--white); font-size: 44px; font-weight: 400; letter-spacing: 0.5px;
  }

  .profile-list { position: absolute; left: 0; top: 130px; width: 1200px; }
  .profile { position: absolute; left: 0; width: 1200px; }
  .profile:nth-child(1) { top: 0; }
  .profile:nth-child(2) { top: 151px; }
  .profile:nth-child(3) { top: 304px; }
  .profile:nth-child(4) { top: 460px; }

  .profile-marker { position: absolute; left: 30px; top: 0; width: 34px; height: 34px; }
  .profile-title {
    position: absolute; left: 83px; top: 3px;
    color: var(--title-blue); font-size: 27px; font-weight: 400; white-space: nowrap;
  }
  .profile-text {
    position: absolute; left: 83px; top: 45px; width: 1080px;
    color: var(--body-grey); font-size: 19.5px; line-height: 32px; white-space: nowrap;
  }

  .slide-footer {
    position: absolute; left: 0; top: 850px; width: 1200px; height: 50px;
    background: var(--brand-blue);
  }
  .footer-url {
    position: absolute; left: 13px; top: 12px;
    color: var(--white); font-size: 23px;
  }
  .footer-brand {
    position: absolute; right: 16px; top: 7px;
    display: flex; align-items: center; gap: 8px;
    color: var(--white); font-size: 32px;
  }
  .footer-brand svg { width: 26px; height: 26px; }
</style>
</head>
<body>
<main class="slide">
  <header class="slide-header" role="img" aria-label="Blue banner with faint connected technology icons">
    <h1 class="slide-title">PROJECT TITLE HERE</h1>
  </header>

  <section class="profile-list">
    <article class="profile">
      <svg class="profile-marker" viewBox="0 0 34 34" aria-hidden="true"><circle cx="17" cy="17" r="16" fill="var(--brand-blue)"/></svg>
      <h2 class="profile-title">BUSINESS PROFILE TITLE HERE</h2>
      <p class="profile-text">Subtext here Subtext here Subtext here Subtext here Subtext here Subtext here Subtext here Subtext here Subtext<br>here Subtext here Subtext here Subtext here Subtext here Subtext here Subtext here Subtext here</p>
    </article>
    <article class="profile">
      <svg class="profile-marker" viewBox="0 0 34 34" aria-hidden="true"><circle cx="17" cy="17" r="16" fill="var(--brand-blue)"/></svg>
      <h2 class="profile-title">BUSINESS PROFILE TITLE HERE</h2>
      <p class="profile-text">Subtext here Subtext here Subtext here Subtext here Subtext here Subtext here Subtext here Subtext here Subtext<br>here Subtext here Subtext here Subtext here Subtext here Subtext here Subtext here Subtext here</p>
    </article>
    <article class="profile">
      <svg class="profile-marker" viewBox="0 0 34 34" aria-hidden="true"><circle cx="17" cy="17" r="16" fill="var(--brand-blue)"/></svg>
      <h2 class="profile-title">BUSINESS PROFILE TITLE HERE</h2>
      <p class="profile-text">Subtext here Subtext here Subtext here Subtext here Subtext here Subtext here Subtext here Subtext here Subtext<br>here Subtext here Subtext here Subtext here Subtext here Subtext here Subtext here Subtext here</p>
    </article>
    <article class="profile">
      <svg class="profile-marker" viewBox="0 0 34 34" aria-hidden="true"><circle cx="17" cy="17" r="16" fill="var(--brand-blue)"/></svg>
      <h2 class="profile-title">BUSINESS PROFILE TITLE HERE</h2>
      <p class="profile-text">Subtext here Subtext here Subtext here Subtext here Subtext here Subtext here Subtext here Subtext here Subtext<br>here Subtext here Subtext here Subtext here Subtext here Subtext here Subtext here Subtext here</p>
    </article>
  </section>

  <footer class="slide-footer">
    <span class="footer-url">www.vantora.com.au</span>
    <span class="footer-brand">Vantora<svg viewBox="0 0 26 26" aria-hidden="true"><circle cx="13" cy="13" r="12" fill="var(--white)"/></svg></span>
  </footer>
</main>
</body>
</html>
```